Ardenwick Tax Advisers Business Card

We are seeking a clean, professional, and modern double sided business card design for Ardenwick Tax Advisers, a tax, accounting, and advisory firm serving business owners, professionals, and investors.
The design should convey credibility, precision, trust, and sophistication appropriate for a CPA level tax advisory firm. Avoid playful, trendy, or overly decorative styles. The look should be sharp, balanced, and timeless.
Our official company logo has been uploaded, which must be incorporated appropriately and consistently with the brand. Designers should not modify, distort, or recreate the logo.
Card format
Standard US business card size (3.5 x 2 inches)
Double sided
Design direction
Professional and modern
Minimalist and uncluttered
Strong typography and clean spacing
Subtle visual interest is welcome, but simplicity is preferred
High contrast and readability are critical
Front side
Primary focus on the Ardenwick Tax Advisers logo
The firm name should be clearly legible and visually prominent
Background may be white or dark, depending on what best complements the logo
Back side
Contact information layout, such as
Name: Martin G. Pellow, MSA, CFP®, AIF®, EA
Title: Managing Director, Tax
Email: mpellow@myardenwick-example.net
Website: https://www.corvelfirm-example.tax/
Mobile: (480) 555-0132
Direct: (817) 555-0187
Main: (817) 555-0149
Address: 3807 Fenwick Rd., Suite 118, Grapevine, TX 76099
Icons may be used sparingly if they enhance clarity
The layout should feel organized and structured
Color and style
Use colors that complement the uploaded logo
Neutral, professional tones preferred
Avoid loud or saturated colors
The design should print well on standard cardstock
Print considerations
Design should be print‑ready
No edge to edge elements that risk being cut off
Proper margins and bleed awareness
Overall, the goal is a polished, high end business card that reflects trust, expertise, and professionalism consistent with a firm providing tax strategy, compliance, and advisory services.

```html
<!DOCTYPE html>
<html lang="en">
<head>
<meta charset="utf-8">
<title>Ardenwick Tax Advisers – Business Card</title>
<link href="https://fonts.googleapis.com/css2?family=Poppins:wght@400;500;600;700&display=swap" rel="stylesheet">
<style>
  :root {
    --stage: #333333;
    --paper: #f8f8f8;
    --navy: #21245a;
    --orange: #f27a2a;
    --white: #ffffff;
    --rule: rgba(255,255,255,0.85);
  }
  * { margin: 0; padding: 0; box-sizing: border-box; }
  html, body { width: 1200px; height: 1200px; overflow: hidden; }
  body {
    background: var(--stage);
    font-family: "Poppins", sans-serif;
    position: relative;
  }
  .card {
    position: absolute;
    left: 231px;
    width: 738px;
    height: 421px;
  }
  .card--front { top: 145px; background: var(--paper); }
  .card--back { top: 634px; background: var(--navy); color: var(--white); }

  .brand {
    position: absolute;
    inset: 0;
    display: flex;
    align-items: center;
    justify-content: center;
    gap: 16px;
  }
  .brand__dot {
    width: 20px; height: 20px;
    border-radius: 50%;
    background: var(--navy);
  }
  .brand__name {
    font-weight: 600;
    font-size: 36px;
    letter-spacing: 2px;
    color: var(--navy);
    white-space: nowrap;
  }

  .contact {
    position: absolute;
    left: 255px;
    top: 0;
    width: 356px;
    height: 100%;
  }
  .contact__name {
    position: absolute;
    top: 94px; left: 2px;
    transform: translateY(-50%);
    font-weight: 700;
    font-size: 20px;
    color: var(--orange);
    white-space: nowrap;
  }
  .contact__title {
    position: absolute;
    top: 128px; left: 2px;
    transform: translateY(-50%);
    font-size: 18px;
    white-space: nowrap;
  }
  .row {
    position: absolute;
    left: 2px;
    display: flex;
    align-items: center;
    gap: 8px;
    font-size: 14.5px;
    white-space: nowrap;
    transform: translateY(-50%);
  }
  .row svg { width: 12px; height: 12px; flex: none; }
  .rule {
    position: absolute;
    left: 0; width: 356px; height: 1px;
    background: var(--rule);
  }
</style>
</head>
<body>
  <section class="card card--front">
    <div class="brand">
      <span class="brand__dot"></span>
      <span class="brand__name">Ardenwick Tax Advisers</span>
    </div>
  </section>

  <section class="card card--back">
    <div class="contact">
      <p class="contact__name">Martin G. Pellow, MSA, CFP®, AIF®, EA</p>
      <p class="contact__title">Managing Director, Tax</p>

      <p class="row" style="top:172px">
        <svg viewBox="0 0 24 24"><path fill="#f27a2a" d="M6.6 10.8a15.2 15.2 0 0 0 6.6 6.6l2.2-2.2a1 1 0 0 1 1-.25 11.4 11.4 0 0 0 3.6.57 1 1 0 0 1 1 1V20a1 1 0 0 1-1 1A17 17 0 0 1 3 4a1 1 0 0 1 1-1h3.5a1 1 0 0 1 1 1c0 1.25.2 2.45.57 3.57a1 1 0 0 1-.25 1z"/></svg>
        (817) 555-0149
      </p>
      <div class="rule" style="top:188px"></div>

      <p class="row" style="top:212px">
        <svg viewBox="0 0 24 24"><rect x="6" y="2" width="12" height="20" rx="2" fill="none" stroke="#f27a2a" stroke-width="2" transform="rotate(-25 12 12)"/></svg>
        (480) 555-0132
      </p>
      <p class="row" style="top:239px">
        <svg viewBox="0 0 24 24"><path fill="#f27a2a" d="M6.6 10.8a15.2 15.2 0 0 0 6.6 6.6l2.2-2.2a1 1 0 0 1 1-.25 11.4 11.4 0 0 0 3.6.57 1 1 0 0 1 1 1V20a1 1 0 0 1-1 1A17 17 0 0 1 3 4a1 1 0 0 1 1-1h3.5a1 1 0 0 1 1 1c0 1.25.2 2.45.57 3.57a1 1 0 0 1-.25 1z"/></svg>
        (817) 555-0187
      </p>
      <div class="rule" style="top:259px"></div>

      <p class="row" style="top:276px">
        <svg viewBox="0 0 24 24"><rect x="2" y="5" width="20" height="14" fill="none" stroke="#f27a2a" stroke-width="2"/><path d="M2 5l10 8 10-8" fill="none" stroke="#f27a2a" stroke-width="2"/></svg>
        mpellow@myardenwick-example.net
      </p>
      <p class="row" style="top:304px">
        <svg viewBox="0 0 24 24"><g fill="none" stroke="#f27a2a" stroke-width="2"><circle cx="12" cy="12" r="10"/><ellipse cx="12" cy="12" rx="4" ry="10"/><path d="M2 12h20"/></g></svg>
        www.ardenwick-example.tax
      </p>
      <div class="rule" style="top:322px"></div>

      <p class="row" style="top:339px">
        <svg viewBox="0 0 24 24"><path fill="#f27a2a" d="M12 2a7 7 0 0 0-7 7c0 5.2 7 13 7 13s7-7.8 7-13a7 7 0 0 0-7-7zm0 9.5A2.5 2.5 0 1 1 12 6.5a2.5 2.5 0 0 1 0 5z"/></svg>
        3807 Fenwick Rd., Suite 118, Grapevine, TX 76099
      </p>
    </div>
  </section>
</body>
</html>
```